Exciting & Elegant Stationary Pack

Stationary consists of
1. Letter head / Envelope
2. Business Card
3. Invoice
4. 40x40mm sticker

Attached files;

1. Logo (Other formats available on request)
2. MS word Doc - For information and description of design
3. Website image (This will be our new website so use the colours so everything ties together)
4. Sample of stationary pack we like, but feel free to be creative

Target Market(s)

Home improvement

Industry/Entity Type

Construction

Other font styles liked:
• Leave up to designer - We like font used on (website attached image)

Requirements
Must have
• Please look at uploaded file of sample website and use colours
Nice to have
• Any type of business card design - eg. metal, die cut, embossed, etc...

```html
<!DOCTYPE html>
<html lang="en">
<head>
<meta charset="utf-8">
<title>Setline Tiling – Business Card</title>
<link href="https://fonts.googleapis.com/css2?family=Source+Sans+3:wght@400;700&display=swap" rel="stylesheet">
<style>
  :root {
    --backdrop: #6e6e6e;
    --card-light: #d7d7d7;
    --navy: #0d3f68;
    --orange: #f08a2e;
    --ink: #2a2a2a;
    --white: #ffffff;
    --divider: #555555;
  }
  * { box-sizing: border-box; margin: 0; padding: 0; }
  html, body {
    width: 1200px; height: 750px; overflow: hidden;
    background: var(--backdrop);
    font-family: "Source Sans 3", "Helvetica Neue", Arial, sans-serif;
  }
  .canvas { position: relative; width: 1200px; height: 750px; }

  .card { position: absolute; width: 461px; height: 263px; }
  .card--front { left: 308px; top: 105px; background: var(--card-light); }
  .card--back  { left: 475px; top: 413px; background: var(--navy); }

  .brand {
    position: absolute; display: flex; align-items: center; gap: 8px;
    font-weight: 700; font-size: 26px; letter-spacing: 0.5px; line-height: 1;
  }
  .brand__mark { width: 14px; height: 14px; }
  .card--front .brand { left: 30px; top: 116px; color: var(--navy); }
  .card--front .brand__mark { background: var(--navy); }
  .card--back .brand { right: 34px; bottom: 52px; color: var(--white); }
  .card--back .brand__mark { background: var(--white); }

  .divider {
    position: absolute; left: 232px; top: 70px;
    width: 1px; height: 136px; background: var(--divider);
  }

  .contact { position: absolute; left: 252px; top: 76px; color: var(--ink); }
  .contact__name { font-size: 19px; font-weight: 700; color: var(--navy); line-height: 1.1; }
  .contact__role { font-size: 14px; color: var(--orange); line-height: 1.3; }
  .contact__licence { font-size: 13.5px; margin-top: 8px; }
  .contact__list { list-style: none; margin-top: 10px; }
  .contact__item {
    display: flex; align-items: center; gap: 6px;
    font-size: 13.5px; line-height: 18px;
  }
  .contact__icon { width: 12px; height: 12px; flex: none; }
</style>
</head>
<body>
<main class="canvas">

  <section class="card card--front" aria-label="Business card front">
    <div class="brand"><span class="brand__mark"></span>Setline Tiling</div>
    <div class="divider"></div>
    <div class="contact">
      <p class="contact__name">Linh Tran</p>
      <p class="contact__role">Project Manager</p>
      <p class="contact__licence">Lic No.,204519c</p>
      <ul class="contact__list">
        <li class="contact__item">
          <svg class="contact__icon" viewBox="0 0 12 12" aria-hidden="true">
            <rect x="3" y="0.5" width="6.5" height="11" rx="1" fill="none" stroke="#0d3f68" stroke-width="1.3"/>
            <rect x="4.5" y="9" width="3.5" height="1" fill="#0d3f68"/>
          </svg>0400 555 319</li>
        <li class="contact__item">
          <svg class="contact__icon" viewBox="0 0 12 12" aria-hidden="true">
            <rect x="0.5" y="2.5" width="11" height="7" fill="#0d3f68"/>
            <path d="M0.5 2.5 L6 7 L11.5 2.5" fill="none" stroke="#d7d7d7" stroke-width="1"/>
          </svg>hello@setlinetiling.com.au</li>
        <li class="contact__item">
          <svg class="contact__icon" viewBox="0 0 12 12" aria-hidden="true">
            <circle cx="6" cy="6" r="5.5" fill="#0d3f68"/>
            <ellipse cx="6" cy="6" rx="2.3" ry="5.5" fill="none" stroke="#d7d7d7" stroke-width="0.8"/>
            <line x1="0.5" y1="6" x2="11.5" y2="6" stroke="#d7d7d7" stroke-width="0.8"/>
          </svg>www.setlinetiling.com.au</li>
      </ul>
    </div>
  </section>

  <section class="card card--back" aria-label="Business card back">
    <div class="brand"><span class="brand__mark"></span>Setline Tiling</div>
  </section>

</main>
</body>
</html>
```